Lakeshore Freightways Guild Web Update

Update wordpress based association web site. Please look up www.lakeshorefreightwaysguild.com for our web site to get a feel for what we currently having. We would like our updated web site to look similar to: www.brightoakline.com. We will provide our key points for updating in a future email.

Target Market(s)

duplicate the brightoakline.com format please.

Number of Pages Required

4 page

Font styles to use
Serif

Requirements
Must have
• duplicate the brightoakline.com format please. You will keep most of the content that we currently have on our website.
Nice to have
• n/a
Should not have
• n/a

```html
<!DOCTYPE html>
<html lang="en">
<head>
<meta charset="utf-8">
<title>Lakeshore Freightways Guild</title>
<link href="https://fonts.googleapis.com/css2?family=Arimo:wght@400;700&family=Tinos:wght@700&display=swap" rel="stylesheet">
<style>
:root{
  --navy:#1d1d7e;
  --navy-deep:#15156a;
  --panel:rgba(28,28,120,.86);
  --text:#ffffff;
  --topbar:#ececf2;
  --grey:#666;
  --accent:#d92a2a;
}
*{margin:0;padding:0;box-sizing:border-box}
html,body{width:1200px;height:4145px;overflow:hidden;background:#fff;font-family:"Arimo",Arial,sans-serif;color:var(--grey)}
.topbar{height:24px;background:var(--topbar);display:flex;align-items:center;justify-content:space-between;padding:0 22px;font-size:10px;color:#555}
.topbar .contacts span{margin-right:18px}
.topbar .follow{color:var(--navy);font-weight:700}
.header{height:56px;display:flex;align-items:center;justify-content:space-between;padding:0 22px}
.brand{display:flex;align-items:center;gap:10px;font-family:"Tinos",Georgia,serif;font-weight:700;color:var(--navy)}
.brand .mark{width:30px;height:30px;background:var(--navy)}
.brand .name{font-size:19px;letter-spacing:.5px}
.nav{display:flex;gap:8px}
.nav .menu{border:1px solid #bbb;padding:5px 12px;font-size:12px;color:#555}
.nav .login{background:var(--navy);color:#fff;padding:6px 12px;font-size:12px}
.hero{position:relative;height:575px;background:linear-gradient(160deg,#1d3e7a 0%,#4f78b0 35%,#7a6a5a 65%,#3a3028 100%)}
.hero h1{position:absolute;left:150px;top:160px;width:540px;color:#fff;font-size:21px;line-height:1.45;font-weight:700}
.hero .chev{position:absolute;left:584px;bottom:22px}
.hero .dots{position:absolute;right:60px;bottom:22px;display:flex;gap:8px}
.hero .dots i{width:10px;height:10px;border-radius:50%;background:#fff;display:block}
.hero .dots i.on{background:#3aa0e0}
.section-title{text-align:center;color:var(--navy);font-size:26px;font-weight:700;height:104px;line-height:104px}
.band{position:relative}
.photo{position:absolute;inset:0}
.panel{position:absolute;top:0;bottom:0;background:var(--panel);color:var(--text);padding:48px 30px;font-size:14px;line-height:1.95;letter-spacing:1px;text-align:justify}
.panel.right{left:602px;width:425px}
.panel.left{left:171px;width:440px}
.sign{display:flex;justify-content:flex-end;align-items:center;gap:14px;margin-top:6px;font-weight:700;text-align:right;line-height:1.4}
.sign .portrait{width:66px;height:66px;border-radius:50%;background:linear-gradient(#8fa3c0,#4a5d7a);border:2px solid #fff}
.inset{margin-top:22px;height:205px;background:linear-gradient(#7aa2d8,#6f8a5a 60%,#5a5a4a)}
.video{position:relative;margin-top:28px;height:205px;background:linear-gradient(135deg,#3a3028,#7a6040 50%,#d0a870)}
.video .play{position:absolute;left:50%;top:50%;transform:translate(-50%,-50%)}
.btn-outline{display:inline-block;border:2px solid #fff;color:#fff;padding:10px 18px;font-size:15px;margin-top:30px;letter-spacing:0}
.field{background:#fff;color:#888;height:44px;line-height:44px;padding:0 12px;font-size:14px;margin-top:14px;letter-spacing:0}
.subscribe{display:inline-block;border:2px solid #fff;padding:8px 34px;margin-top:50px;font-size:15px;letter-spacing:0}
.footer{height:202px;background:var(--navy);display:flex;align-items:center;justify-content:space-between;padding:0 60px;color:#fff}
.footer .links{display:flex;flex-direction:column;gap:22px}
.footer .links a{display:block;width:200px;border:2px solid #fff;color:#fff;text-align:center;padding:10px 0;font-size:14px;text-decoration:none}
.footer .item{display:flex;flex-direction:column;align-items:center;gap:10px;font-size:13px;font-weight:700;text-align:center;white-space:nowrap;line-height:1.4}
.copy{height:46px;background:var(--navy-deep);display:flex;align-items:center;justify-content:space-between;padding:0 75px;color:#fff;font-size:13px}
</style>
</head>
<body>
<div class="topbar">
  <div class="contacts"><span>48 Harbor Street, Suite 210 Bayport, MI 49001</span><span>(555) 014-2231</span><span>(555) 014-2288</span><span>info@lakeshorefreightwaysguild.com</span></div>
  <div class="follow">Follow us</div>
</div>
<header class="header">
  <div class="brand"><span class="mark"></span><span class="name">Lakeshore Freightways Guild</span></div>
  <nav class="nav"><span class="menu">Menu ☰</span><span class="login">Login</span></nav>
</header>

<section class="hero" role="img" aria-label="Freight locomotive at dusk pulling a long train with headlights on">
  <h1>Every year America's freight railroads spend more than $20 billion annually of their own funds, not taxpayer money, to build and maintain a rail network that is safe, reliable, efficient and affordable.</h1>
  <svg class="chev" width="32" height="16" viewBox="0 0 32 16"><path d="M2 2 L16 14 L30 2" fill="none" stroke="#fff" stroke-width="2"/></svg>
  <div class="dots"><i class="on"></i><i></i><i></i><i></i></div>
</section>

<h2 class="section-title">Welcome to LFG</h2>
<section class="band" style="height:474px">
  <div class="photo" role="img" aria-label="Red freight locomotives beside a railroad crossing signal in snow" style="background:linear-gradient(90deg,#5a4a48 0%,#b8c2d0 30%,#c8d4e4 70%,#7a8aa0 100%)"></div>
  <div class="panel right">
    <p>I would like to welcome you to the Lakeshore Freightways Guild website. Here you will find valuable information on Michigan railroads, including issues and concerns in and around the railroad industry. We are an active and aggressive state railroad association and we look forward to continued success with our partnerships. Please make sure to click on our member railroad company links while you're here. Also, sign up for our newsletter and follow the LFG on social media. Thank you and I hope you enjoy your visit to our website.</p>
    <div class="sign"><span>Dana Whitfield<br>President</span><span class="portrait" role="img" aria-label="Portrait of the president"></span></div>
  </div>
</section>

<h2 class="section-title">What We DO</h2>
<section class="band" style="height:563px">
  <div class="photo" role="img" aria-label="Business people reviewing documents at a desk" style="background:linear-gradient(90deg,#c8ccd4 0%,#8a96a8 50%,#5a6478 100%)"></div>
  <div class="panel left">
    <p>The LFG reviews all introduced legislation in the House and Senate. Proposed legislation affecting the rail industry is shared with our members. Final industry positions regarding legislation are then communicated to the legislature. We pursue the same activity with appropriate personnel in the state departments and the legislative rules process.</p>
    <div class="inset" role="img" aria-label="Freight locomotives on a rail line under blue sky"></div>
  </div>
</section>

<h2 class="section-title">Who We Are</h2>
<section class="band" style="height:566px">
  <div class="photo" role="img" aria-label="Railroad tracks with signal gantry among green trees" style="background:linear-gradient(90deg,#8aa0b8 0%,#6a7a5a 30%,#9aa08a 60%,#3a3a3a 100%)"></div>
  <div class="panel right">
    <p>The Lakeshore Freightways Guild (LFG) is a non-profit trade association that represents the interests of freight railroads operating in Michigan. LFG members range in size from large Class 1 interstate carriers to smaller regional carriers and shortline railroads. LFG members account for over 95% of all freight rail moved in Michigan.</p>
    <div class="video" role="img" aria-label="Video thumbnail of a steam locomotive near a station">
      <svg class="play" width="44" height="32" viewBox="0 0 44 32"><rect width="44" height="32" rx="7" fill="#fff"/><path d="M17 9 L29 16 L17 23Z" fill="#222"/></svg>
    </div>
  </div>
</section>

<h2 class="section-title">How to Join LFG</h2>
<section class="band" style="height:563px">
  <div class="photo" role="img" aria-label="Freight train passing through green trees beside a lake" style="background:linear-gradient(90deg,#4a6a3a 0%,#7a9a6a 40%,#9ab0c8 70%,#3a5a3a 100%)"></div>
  <div class="panel left">
    <p>LFG membership is open to any freight railroad with Michigan operations. Please contact the LFG office for membership information. Companies which supply goods or services to the railroad industry are eligible for a non-voting Associate Membership. Annual dues are $1,000 per year for supplier members.</p>
    <p style="margin-top:22px">Please click <span style="color:var(--accent);font-weight:700">HERE</span> to download the LFG Associate Membership application. Return a completed form to: info@lakeshorefreightwaysguild.com or mail to our mailing address.</p>
    <span class="btn-outline">Meet our Members</span>
  </div>
</section>

<h2 class="section-title">Newsletter</h2>
<section class="band" style="height:442px">
  <div class="photo" role="img" aria-label="Freight locomotive passing a signal mast on a wooded line" style="background:linear-gradient(90deg,#5a6a4a 0%,#8a9a7a 40%,#a8b898 80%,#7a8a6a 100%)"></div>
  <div class="panel right" style="padding-top:70px">
    <p>Subscribe to our Newsletter and receive latest updates.</p>
    <div class="field">Name*</div>
    <div class="field">Email*</div>
    <span class="subscribe">Subscribe</span>
  </div>
</section>

<h2 class="section-title" style="height:80px;line-height:80px">Contact Us</h2>
<footer class="footer">
  <div class="links"><a>RESOURCES</a><a>RAILROADS &amp; VETERANS</a></div>
  <div class="item">
    <svg width="24" height="30" viewBox="0 0 24 30"><path d="M12 28 C4 18 2 14 2 10 A10 10 0 0 1 22 10 C22 14 20 18 12 28Z" fill="none" stroke="#fff" stroke-width="2"/><circle cx="12" cy="10" r="3.5" fill="none" stroke="#fff" stroke-width="2"/></svg>
    <span>48 Harbor Street,<br>Suite 210 Bayport, MI 49001</span>
  </div>
  <div class="item">
    <svg width="28" height="28" viewBox="0 0 28 28"><path d="M6 3 L11 3 L13 9 L10 11 C12 16 14 18 18 20 L20 17 L26 19 L26 24 C14 26 2 14 4 3Z" fill="none" stroke="#fff" stroke-width="2"/></svg>
    <span>(555) 014-2231</span>
  </div>
  <div class="item">
    <svg width="28" height="28" viewBox="0 0 28 28"><rect x="3" y="11" width="22" height="12" fill="none" stroke="#fff" stroke-width="2"/><rect x="8" y="3" width="12" height="8" fill="none" stroke="#fff" stroke-width="2"/><line x1="8" y1="17" x2="20" y2="17" stroke="#fff" stroke-width="2"/></svg>
    <span>(555) 014-2288</span>
  </div>
  <div class="item">
    <svg width="30" height="24" viewBox="0 0 30 24"><rect x="2" y="3" width="26" height="18" fill="none" stroke="#fff" stroke-width="2"/><path d="M2 3 L15 14 L28 3" fill="none" stroke="#fff" stroke-width="2"/></svg>
    <span>info@lakeshorefreightwaysguild.com</span>
  </div>
</footer>
<div class="copy"><span>© Copyright 2017. LFG. All rights reserved.</span><span>Follow us</span></div>
</body>
</html>
```